hi all

Im after a new age looking business card with my company logo on it

must include these details, I would like the PH and Email to be symbols

If the colours used for card could be kept within the colours used in logo that I have supplied that would be great, if another colour is to be used dark grey would be ok. no light bulbs etc thanks

Details below to be incorporated on card

Damian Holloway

Lic E871302

PH 0219647381

E info@brightvaleelectrical.example.nz

Domestic Commercial Industrial Electricians

```html
<!DOCTYPE html>
<html lang="en">
<head>
<meta charset="utf-8">
<title>Brightvale Electrical – Business Card</title>
<link href="https://fonts.googleapis.com/css2?family=Michroma&family=Poppins:wght@400&display=swap" rel="stylesheet">
<style>
  :root {
    --backdrop: #2a2a2c;
    --card: #151516;
    --card-edge: #0c0c0d;
    --brand-blue: #1a7ac4;
    --text-white: #f2f2f2;
    --text-silver: #d9d9d9;
    --rule: #bdbdbd;
    --emboss: #1b1b1c;
    --emboss-line: #2a2a2c;
  }
  * { margin: 0; padding: 0; box-sizing: border-box; }
  html, body {
    width: 1200px; height: 900px; overflow: hidden;
    background: var(--backdrop);
  }
  .canvas {
    width: 1200px; height: 900px;
    display: flex; flex-direction: column;
    align-items: center; justify-content: center; gap: 30px;
  }
  .card {
    position: relative; width: 720px; height: 411px; flex: none;
    background: var(--card);
    border: 1px solid var(--card-edge);
    box-shadow: 0 16px 40px rgba(0,0,0,.55);
    overflow: hidden;
    font-family: "Poppins", sans-serif;
    color: var(--text-white);
  }

  /* Front */
  .emboss-mark {
    position: absolute; right: -40px; top: 90px;
    width: 300px; height: 240px; border-radius: 50%;
    background: var(--emboss);
    border: 2px solid var(--emboss-line);
    box-shadow: inset 2px 3px 6px rgba(0,0,0,.6);
  }
  .brand {
    position: absolute; left: 180px; top: 44px;
    display: flex; align-items: center; gap: 14px;
  }
  .brand-dot {
    width: 54px; height: 54px; border-radius: 50%;
    border: 3px solid var(--brand-blue); flex: none;
  }
  .brand-name {
    font-family: "Michroma", sans-serif; font-weight: 400;
    color: var(--brand-blue);
    font-size: 28px; line-height: 1.15; letter-spacing: 1px;
    text-transform: uppercase;
  }
  .brand-name span { display: block; font-size: 12px; letter-spacing: 8px; }
  .divider {
    position: absolute; left: 30px; right: 70px; top: 150px;
    height: 1px; background: var(--rule);
  }
  .person { position: absolute; left: 40px; top: 164px; }
  .person-name {
    font-family: "Michroma", sans-serif;
    font-size: 15px; letter-spacing: 1px; text-transform: uppercase;
  }
  .person-licence { margin-top: 2px; font-size: 13px; color: var(--brand-blue); }
  .contacts {
    position: absolute; right: 44px; top: 262px; list-style: none;
  }
  .contacts li {
    display: flex; align-items: center; justify-content: flex-end;
    gap: 10px; font-size: 13px; line-height: 26px;
  }
  .contact-icon {
    width: 18px; height: 18px; border-radius: 3px;
    background: var(--brand-blue);
    display: flex; align-items: center; justify-content: center;
  }
  .service-band {
    position: absolute; left: 0; right: 0; bottom: 0; height: 46px;
    background: var(--brand-blue);
    display: flex; align-items: center; justify-content: space-between;
    padding: 0 44px 0 90px;
  }
  .service-band p {
    font-family: "Michroma", sans-serif;
    font-size: 13px; letter-spacing: 1px; text-transform: uppercase;
    white-space: nowrap; color: var(--text-white);
  }

  /* Back */
  .card-back { display: flex; align-items: center; justify-content: center; }
  .back-brand { display: flex; align-items: center; gap: 16px; }
  .back-brand .brand-dot { width: 64px; height: 64px; border-color: var(--text-silver); }
  .back-brand .brand-name { color: var(--text-silver); font-size: 34px; }
  .back-brand .brand-name span { font-size: 14px; letter-spacing: 10px; }
</style>
</head>
<body>
<main class="canvas">
  <section class="card card-front" aria-label="Business card front">
    <div class="emboss-mark" aria-hidden="true"></div>

    <header class="brand">
      <div class="brand-dot" aria-hidden="true"></div>
      <h1 class="brand-name">Brightvale<span>Electrical</span></h1>
    </header>

    <div class="divider"></div>

    <div class="person">
      <p class="person-name">Damian Holloway</p>
      <p class="person-licence">Lic E871302</p>
    </div>

    <ul class="contacts">
      <li>0219647381
        <span class="contact-icon">
          <svg width="11" height="11" viewBox="0 0 24 24"><path fill="#151516" d="M6.6 10.8a15 15 0 0 0 6.6 6.6l2.2-2.2a1 1 0 0 1 1-.25 11.4 11.4 0 0 0 3.6.57 1 1 0 0 1 1 1V20a1 1 0 0 1-1 1A17 17 0 0 1 3 4a1 1 0 0 1 1-1h3.5a1 1 0 0 1 1 1c0 1.25.2 2.45.57 3.57a1 1 0 0 1-.25 1z"/></svg>
        </span>
      </li>
      <li>info@brightvaleelectrical.example.nz
        <span class="contact-icon">
          <svg width="11" height="11" viewBox="0 0 24 24"><rect x="2" y="5" width="20" height="14" rx="1" fill="none" stroke="#151516" stroke-width="2.6"/><path d="M2 6l10 7 10-7" fill="none" stroke="#151516" stroke-width="2.6"/></svg>
        </span>
      </li>
    </ul>

    <footer class="service-band">
      <p>Domestic Commercial Industrial Electricians</p>
      <svg width="16" height="22" viewBox="0 0 22 30" aria-hidden="true"><path d="M14 0L2 17h8l-4 13L20 11h-8z" fill="#151516"/></svg>
    </footer>
  </section>

  <section class="card card-back" aria-label="Business card back">
    <div class="back-brand">
      <div class="brand-dot" aria-hidden="true"></div>
      <p class="brand-name">Brightvale<span>Electrical</span></p>
    </div>
  </section>
</main>
</body>
</html>
```